Used Car Dealer seeks an Amazing Business Card Design

We are looking for a business card design that incorporates our logo and grabs the attention of anyone we give the business card to.

Looking to use the same colors as the logo. Our Logo choice is the black background with Red and Silver/Grey Lettering.

We also would like to see some embossed designs.

Target Market(s)

Used Car Buyers, Automotive, Auto

Industry/Entity Type

Automotive

Contact Information for Business Card

BVEX7K
Gordon Whitley
482 Tenbrook Lane
Suite 305
Roswell, GA 30098
Office (770) 555-0142
Cell (770) 555-0187
bvex7kga@mailnest.example
www.bvex7kga.example

Colors
ffffff
ee3036

Requirements
Must have
• Must include our logo (Black Background with Red and Silver/Grey Lettering)
Nice to have
• Embossed Design. Can be Single or Double Sided.

```html
<!DOCTYPE html>
<html lang="en">
<head>
<meta charset="UTF-8">
<title>BVEX7K Business Card</title>
<link rel="stylesheet" href="https://fonts.googleapis.com/css2?family=Open+Sans:ital,wght@0,400;0,600;1,400;1,600&display=swap">
<style>
  :root {
    --stage: #8b8c8e;
    --card-red: #ee3036;
    --card-slate: #4f5b6a;
    --card-white: #ffffff;
    --silver: #d9dbde;
  }
  html, body {
    margin: 0;
    padding: 0;
    width: 1200px;
    height: 817px;
    overflow: hidden;
    background: var(--stage);
  }
  .stage {
    position: relative;
    width: 1200px;
    height: 817px;
  }
  .card {
    position: absolute;
    left: 150px;
    top: 151px;
    width: 900px;
    height: 514px;
    overflow: hidden;
    font-family: "Open Sans", Arial, sans-serif;
    box-shadow: 0 18px 40px rgba(0,0,0,0.28);
  }
  .card-art {
    position: absolute;
    inset: 0;
  }
  .contact-details {
    position: absolute;
    left: 90px;
    top: 58px;
    width: 300px;
    margin: 0;
    display: grid;
    grid-template-columns: 78px 1fr;
    column-gap: 8px;
    row-gap: 4px;
    color: var(--card-white);
    font-size: 15px;
    line-height: 22px;
  }
  .contact-label {
    font-style: italic;
    white-space: nowrap;
  }
  .contact-value {
    margin: 0;
    font-weight: 600;
    white-space: nowrap;
  }
  .brand-band {
    position: absolute;
    left: 0;
    bottom: 0;
    width: 100%;
    height: 104px;
    background: var(--card-white);
  }
  .brand-band-name {
    position: absolute;
    left: 96px;
    top: 24px;
    margin: 0;
    color: var(--card-red);
    font-size: 44px;
    font-weight: 400;
    letter-spacing: 1px;
  }
  .brand-mark {
    position: absolute;
    left: 560px;
    top: 228px;
    display: flex;
    align-items: center;
    gap: 16px;
  }
  .brand-mark-dot {
    width: 22px;
    height: 22px;
    border-radius: 50%;
    background: var(--silver);
  }
  .brand-mark-name {
    margin: 0;
    color: var(--silver);
    font-size: 64px;
    font-weight: 600;
    letter-spacing: 2px;
  }
</style>
</head>
<body>
<main class="stage">
  <section class="card" aria-label="BVEX7K business card">
    <svg class="card-art" width="900" height="514" viewBox="0 0 900 514" aria-hidden="true">
      <rect class="field-slate" x="0" y="0" width="900" height="514" fill="var(--card-slate)"/>
      <polygon class="field-red" points="0,0 430,0 430,120 404,138 404,176 430,190 430,514 0,514" fill="var(--card-red)"/>
      <g class="speed-stripes" stroke="var(--card-slate)" stroke-width="4">
        <line x1="22" y1="0" x2="22" y2="514"/>
        <line x1="36" y1="0" x2="36" y2="514"/>
        <line x1="50" y1="0" x2="50" y2="514"/>
      </g>
    </svg>

    <dl class="contact-details">
      <dt class="contact-label">Name :</dt>
      <dd class="contact-value">Gordon Whitley</dd>
      <dt class="contact-label">Address :</dt>
      <dd class="contact-value">482 Tenbrook Lane, Suite 305<br>Roswell, GA 30098</dd>
      <dt class="contact-label">Phone :</dt>
      <dd class="contact-value">(770) 555-0142</dd>
      <dt class="contact-label">Cell :</dt>
      <dd class="contact-value">(770) 555-0187</dd>
      <dt class="contact-label">Email :</dt>
      <dd class="contact-value">bvex7kga@mailnest.example</dd>
      <dt class="contact-label">Website :</dt>
      <dd class="contact-value">www.bvex7kga.example</dd>
    </dl>

    <div class="brand-mark">
      <span class="brand-mark-dot"></span>
      <p class="brand-mark-name">BVEX7K</p>
    </div>

    <div class="brand-band">
      <p class="brand-band-name">BVEX7K</p>
    </div>
  </section>
</main>
</body>
</html>
```